Kelderby Farm

Need a nice simple clean double sided business card that has our logo and info on:
Kelder By Farm
Martin & Lydia Okerlund
kelderbyfarm@examplemail.test
Martin: 1-555-218-4391
Lydia: 1-555-903-2657
Instagram @ kelderby_farm

Contact Information for Business Card

Martin & Lydia Okerlund kelderbyfarm@examplemail.test Martin: 1-555-218-4391 Lydia: 1-555-903-2657

```html
<!DOCTYPE html>
<html lang="en">
<head>
<meta charset="utf-8">
<title>Kelder By Farm – Business Card</title>
<link href="https://fonts.googleapis.com/css2?family=Montserrat:wght@400;700&display=swap" rel="stylesheet">
<style>
  :root {
    --backdrop: #9c9c9c;
    --paper: #ffffff;
    --farm-green: #68a344;
    --wheat-orange: #f5a31a;
    --ink: #333333;
  }
  html, body {
    margin: 0;
    padding: 0;
    width: 1021px;
    height: 1200px;
    overflow: hidden;
    background: var(--backdrop);
    font-family: "Montserrat", sans-serif;
  }
  .canvas {
    position: relative;
    width: 1021px;
    height: 1200px;
  }
  .card {
    position: absolute;
    width: 753px;
    height: 429px;
    box-sizing: border-box;
  }
  .card-front {
    left: 134px;
    top: 119px;
    background: var(--paper);
  }
  .card-back {
    left: 131px;
    top: 651px;
    background: var(--farm-green);
  }
  .brand {
    position: absolute;
    display: flex;
    flex-direction: column;
    align-items: center;
  }
  .brand-circle {
    border-radius: 50%;
    box-sizing: border-box;
  }
  .brand-name {
    font-weight: 700;
    letter-spacing: 0.5px;
    white-space: nowrap;
    text-transform: uppercase;
  }
  .card-front .brand {
    left: 452px;
    width: 267px;
    top: 35px;
  }
  .card-front .brand-circle {
    width: 104px;
    height: 104px;
    border: 3px solid var(--farm-green);
  }
  .card-front .brand-name {
    margin-top: 10px;
    font-size: 24px;
    color: var(--farm-green);
  }
  .card-back .brand {
    left: 0;
    width: 753px;
    top: 134px;
  }
  .card-back .brand-circle {
    width: 100px;
    height: 100px;
    border: 3px solid var(--paper);
  }
  .card-back .brand-name {
    margin-top: 14px;
    font-size: 32px;
    color: var(--paper);
  }
  .owners {
    position: absolute;
    left: 35px;
    top: 225px;
    margin: 0;
    font-weight: 700;
    font-size: 29px;
    line-height: 36px;
    letter-spacing: 0.5px;
    text-transform: uppercase;
  }
  .owners .given { color: var(--farm-green); display: block; }
  .owners .family { color: var(--wheat-orange); display: block; }
  .divider {
    position: absolute;
    left: 35px;
    width: 682px;
    top: 313px;
    height: 1px;
    background: var(--wheat-orange);
  }
  .phones {
    position: absolute;
    left: 35px;
    top: 330px;
    font-size: 21px;
    color: var(--ink);
    white-space: nowrap;
  }
  .phones .sep {
    display: inline-block;
    width: 1px;
    height: 16px;
    background: var(--wheat-orange);
    margin: 0 12px 0 14px;
    vertical-align: -1px;
  }
  .online {
    position: absolute;
    left: 35px;
    top: 366px;
    font-size: 17px;
    color: var(--ink);
    display: flex;
    align-items: center;
    white-space: nowrap;
  }
  .online svg { margin-right: 6px; }
  .online .handle-mark {
    width: 11px;
    height: 11px;
    border: 1.5px solid var(--farm-green);
    margin: 0 7px 0 16px;
  }
</style>
</head>
<body>
<div class="canvas">
  <section class="card card-front" aria-label="Business card front">
    <div class="brand">
      <div class="brand-circle"></div>
      <div class="brand-name">Kelder By Farm</div>
    </div>
    <h1 class="owners">
      <span class="given">Martin &amp; Lydia</span>
      <span class="family">Okerlund</span>
    </h1>
    <div class="divider"></div>
    <div class="phones">Martin: 1-555-218-4391<span class="sep"></span>Lydia: 1-555-903-2657</div>
    <div class="online">
      <svg width="15" height="11" viewBox="0 0 15 11" aria-hidden="true">
        <rect x="0" y="0" width="15" height="11" fill="#68a344"/>
        <path d="M0 0 L7.5 6 L15 0" fill="none" stroke="#ffffff" stroke-width="1.4"/>
      </svg>
      kelderbyfarm@examplemail.test
      <span class="handle-mark"></span>
      @ kelderby_farm
    </div>
  </section>

  <section class="card card-back" role="img" aria-label="Green card back with faint repeating pattern and centred farm name">
    <div class="brand">
      <div class="brand-circle"></div>
      <div class="brand-name">Kelder By Farm</div>
    </div>
  </section>
</div>
</body>
</html>
```